Help our Crumb Parlour find our winning design! We're looking for a business card....

We’re a Crumb Parlour in NY specializing in custom-made cakes and unique desserts.
Our cakes combine flavor and art, each designed to match customer’s special event and theme.
We’d like a unique business card with a clean design that will combine French chic and artistic look & feel.
We’d like to differentiate ourselves from standard bakeries, please don’t offer cupcake images :-)
Our logo is peach-pink and brown and we’d love to use these colors ( . Another color that can be added is gold - or feel free to suggest!

Target Market(s)

Women, ages 25-55

Industry/Entity Type

Boutique

Contact Information for Business Card

Text on card:
Logo
Crumb Parlour by Dana Whitfield

www.xxxxxxxx.com
xxx@xxxxx.com
(516) xxx-xxxx
F – xxxxxxxxxx
IG - xxxxxxxxx

Font styles to use
Sans Serif
Script

Requirements
Must have
• Logo
• Clean look
• French chic and artistic look & feel.
Nice to have
• Damask pattern
Should not have
• Cupcake images

```html
<!DOCTYPE html>
<html lang="en">
<head>
<meta charset="utf-8">
<title>Crumb Parlour by Dana Whitfield – Business Card</title>
<link rel="stylesheet" href="https://fonts.googleapis.com/css2?family=Lobster&family=Exo+2:wght@500;600&display=swap">
<style>
  :root {
    --paper: #eeebe8;
    --halo: #f1eeeb;
    --peach: #f4b2a1;
    --peach-band: #f2a998;
    --cocoa: #3b2a24;
  }
  * { margin: 0; padding: 0; box-sizing: border-box; }
  html, body { width: 1200px; height: 747px; overflow: hidden; background: var(--paper); }
  .card { position: relative; width: 1200px; height: 747px; background: var(--paper); overflow: hidden; }
  .halo {
    position: absolute; left: 280px; top: -20px; width: 620px; height: 560px;
    border-radius: 50%; background: var(--halo);
  }
  .brand-name {
    position: absolute; left: 0; right: 0; top: 118px; text-align: center;
    font-family: "Lobster", cursive; font-size: 64px; color: var(--cocoa); line-height: 1;
  }
  .tagline {
    position: absolute; left: 0; right: 0; top: 206px; text-align: center;
    font-family: "Exo 2", sans-serif; font-weight: 500; font-size: 15px;
    letter-spacing: 3px; color: var(--cocoa);
  }
  .title {
    position: absolute; left: 0; right: 0; top: 232px; text-align: center;
    font-family: "Lobster", cursive; font-size: 41px; line-height: 44px; color: var(--peach);
  }
  .rule {
    position: absolute; left: 292px; width: 557px; height: 0;
    border-top: 2px dotted var(--peach);
  }
  .rule--top { top: 379px; }
  .rule--bottom { top: 457px; }
  .contact {
    position: absolute; left: 0; right: 0; text-align: center;
    font-family: "Exo 2", sans-serif; font-weight: 600; font-size: 28px; color: var(--cocoa);
  }
  .contact--web { top: 386px; line-height: 28px; }
  .contact--phone { top: 471px; }
  .social-band {
    position: absolute; left: 0; top: 521px; width: 1200px; height: 170px;
    background: var(--peach-band); box-shadow: 0 2px 8px rgba(0,0,0,0.35);
  }
  .social-list { position: absolute; left: 403px; top: 48px; list-style: none; }
  .social-item {
    display: flex; align-items: center; height: 41px;
    font-family: "Exo 2", sans-serif; font-weight: 600; font-size: 28px; color: var(--cocoa);
  }
  .social-mark { width: 32px; height: 32px; border-radius: 5px; background: var(--cocoa); margin-right: 26px; }
</style>
</head>
<body>
<main class="card">
  <div class="halo"></div>

  <div class="brand-name">Velvet Hour</div>
  <div class="tagline">HANDCRAFTED WITH LOVE</div>

  <h1 class="title">Crumb Parlour<br>By<br>Dana Whitfield</h1>

  <div class="rule rule--top"></div>
  <p class="contact contact--web">www.VelvetHourNY.com<br>dana@VelvetHourNY.com</p>
  <div class="rule rule--bottom"></div>
  <p class="contact contact--phone">(516) 555-0182</p>

  <section class="social-band">
    <ul class="social-list">
      <li class="social-item"><span class="social-mark"></span>VelvetHourNYCakes</li>
      <li class="social-item"><span class="social-mark"></span>VelvetHourNYCakes</li>
    </ul>
  </section>
</main>
</body>
</html>
```